Hand sanitizer logos and bottle design

Want a very simple and clean logo for - PURA42.
Need a badge logo for - Clean Shield 42 Keeper.
Need bottle label designed. Mock up is attached. Keep it very clean as in mockup.
Target Market(s)
retail
Font styles to use
Sans Serif
Requirements
Must have
- Simple Clean

```html
<!DOCTYPE html>
<html lang="en">
<head>
<meta charset="UTF-8">
<title>PURA42 Gel Hand Sanitizer Label</title>
<link href="https://fonts.googleapis.com/css2?family=Montserrat:wght@300;400;700;800&family=Orbitron:wght@900&display=swap" rel="stylesheet">
<style>
  :root {
    --brand-orange: #f26a1b;
    --ink: #141414;
    --navy: #1c2a4a;
    --paper: #ffffff;
    --backdrop: #f4f4f4;
    --wash-light: #fff6ec;
    --wash-warm: #fbdcb8;
    --seal-tone: #2b2b2b;
  }
  * { margin: 0; padding: 0; box-sizing: border-box; }
  html, body { width: 1200px; height: 1200px; overflow: hidden; }
  body {
    background: var(--backdrop);
    font-family: "Montserrat", Arial, sans-serif;
    color: var(--ink);
    position: relative;
  }
  .label {
    position: absolute;
    left: 232px; top: 50px;
    width: 736px; height: 1100px;
    background: var(--paper);
    border: 3px solid var(--ink);
    overflow: hidden;
  }
  .backdrop-wash {
    position: absolute; inset: 0;
    background: linear-gradient(160deg, var(--paper) 0%, var(--paper) 22%, var(--wash-light) 45%, var(--wash-warm) 100%);
  }
  .brand-name {
    position: absolute; top: 30px; left: 0; width: 100%;
    text-align: center;
    font-weight: 800; font-size: 140px; line-height: 1;
    color: var(--brand-orange); letter-spacing: -2px;
  }
  .brand-rule {
    position: absolute; top: 204px; left: 247px;
    width: 236px; height: 6px; background: var(--brand-orange);
  }
  .centered { position: absolute; left: 0; width: 100%; text-align: center; }
  .protection-title { top: 244px; font-weight: 300; font-size: 34px; }
  .claim-line { font-weight: 400; font-size: 34px; }
  .claim-top { top: 320px; }
  .claim-bottom { top: 419px; }
  .claim-highlight {
    position: absolute; top: 365px; left: 155px;
    width: 424px; height: 48px;
    background: var(--brand-orange); color: var(--paper);
    font-weight: 700; font-size: 38px; line-height: 48px; text-align: center;
  }
  .guard-badge {
    position: absolute; left: 498px; top: 520px;
    width: 190px; display: flex; align-items: center; gap: 10px;
  }
  .guard-badge .mark { width: 22px; height: 22px; background: var(--brand-orange); flex: none; }
  .guard-badge .name { font-weight: 700; font-size: 24px; line-height: 1.15; color: var(--navy); }
  .product-name {
    position: absolute; left: 54px; top: 525px;
    font-family: "Orbitron", "Arial Black", sans-serif;
    font-weight: 900; font-size: 80px; line-height: 70px;
    color: var(--ink); letter-spacing: 1px;
  }
  .benefits {
    position: absolute; left: 26px; top: 778px;
    list-style: none; font-size: 38px; line-height: 48px; font-weight: 400;
  }
  .benefits li::before {
    content: ""; display: inline-block; width: 13px; height: 13px;
    border-radius: 50%; background: var(--ink); margin-right: 10px;
    vertical-align: middle;
  }
  .cert-seal {
    position: absolute; left: 578px; top: 798px;
    width: 112px; height: 64px;
    background: var(--seal-tone); border-radius: 8px;
  }
  .net-content {
    position: absolute; left: 260px; top: 1030px;
    display: flex; align-items: center; gap: 8px;
  }
  .net-content .unit-label { font-size: 17px; line-height: 16px; font-weight: 400; }
  .net-content .volume { font-weight: 700; font-size: 34px; }
</style>
</head>
<body>
  <main class="label">
    <div class="backdrop-wash" role="img" aria-label="Soft flowing orange wave decoration across the label"></div>

    <h1 class="brand-name">PURA42</h1>
    <div class="brand-rule"></div>

    <p class="centered protection-title">12 HOUR PROTECTION</p>
    <p class="centered claim-line claim-top">Nanotechnology enables one use</p>
    <p class="claim-highlight">12 Hour protection</p>
    <p class="centered claim-line claim-bottom">that will not dry out your skin</p>

    <div class="guard-badge">
      <span class="mark"></span>
      <span class="name">Clean Shield 42 Keeper</span>
    </div>

    <h2 class="product-name">GEL<br>HAND<br>SANITIZER</h2>

    <ul class="benefits">
      <li>non toxic</li>
      <li>alcohol free</li>
      <li>Extended protection</li>
      <li>Kill 99.99% of Viuses</li>
    </ul>

    <div class="cert-seal" role="img" aria-label="Certification seal"></div>

    <div class="net-content">
      <span class="unit-label">CONT<br>NET</span>
      <span class="volume">500 ML.</span>
    </div>
  </main>
</body>
</html>
```